Pricing Poster selling novelty toys and snacks at a Halloween event

I need a poster made for our Halloween event. It would incorporate the items offered and pricing for each.

selling novelty toys and snacks

The Poster needs to say :
PRICE LIST
Bracelets $8 for 1, 4 for $20
Toys $15 for 1, $20 for 2 |
Popcorn $5
Cotton Candy $5
CIDER $4

```html
<!DOCTYPE html>
<html lang="en">
<head>
<meta charset="UTF-8">
<title>Halloween Event Price List</title>
<link href="https://fonts.googleapis.com/css2?family=Chewy&family=Archivo+Black&family=Montserrat:wght@800&display=swap" rel="stylesheet">
<style>
  :root {
    --bg-dark: #120404;
    --bg-red: #4a0a08;
    --orange: #ffa21a;
    --white: #ffffff;
    --ink: #1a0a04;
    --moon: #b3140f;
  }
  html, body {
    margin: 0;
    padding: 0;
    overflow: hidden;
    background: var(--bg-dark);
  }
  .poster {
    position: relative;
    width: 841px;
    height: 1200px;
    overflow: hidden;
    background: radial-gradient(ellipse at 60% 45%, var(--bg-red) 0%, #2a0504 45%, var(--bg-dark) 85%);
    font-family: "Montserrat", Arial, sans-serif;
  }
  .haunted-house {
    position: absolute;
    left: 408px;
    top: 320px;
    width: 420px;
    height: 500px;
    background: linear-gradient(180deg, rgba(70,50,45,0.55) 0%, rgba(45,30,28,0.75) 55%, rgba(25,10,8,0.2) 100%);
    border-radius: 40px 40px 0 0;
  }
  .blood-moon {
    position: absolute;
    left: 547px;
    top: 198px;
    width: 66px;
    height: 66px;
    border-radius: 50%;
    background: radial-gradient(circle at 40% 40%, #d4241a, var(--moon) 60%, #6e0806);
    box-shadow: 0 0 24px rgba(200,20,15,0.6);
  }
  .pumpkins {
    position: absolute;
    left: 0;
    top: 780px;
    width: 841px;
    height: 420px;
    background: radial-gradient(ellipse at 42% 65%, #ffb02e 0%, #e46a08 22%, #8a2a04 45%, rgba(40,8,4,0.6) 70%, rgba(18,4,4,0) 90%);
  }
  .title {
    position: absolute;
    left: 0;
    top: 40px;
    width: 841px;
    height: 150px;
    margin: 0;
  }
  .title-text {
    font-family: "Chewy", "Archivo Black", Arial, sans-serif;
    font-weight: 400;
    font-size: 142px;
    fill: var(--orange);
  }
  .subtitle {
    position: absolute;
    left: 0;
    width: 100%;
    top: 196px;
    margin: 0;
    text-align: center;
    font-family: "Montserrat", Arial, sans-serif;
    font-weight: 800;
    font-size: 54px;
    line-height: 1;
    color: var(--white);
  }
  .price-band {
    position: absolute;
    left: 258px;
    top: 283px;
    width: 327px;
    height: 50px;
    background: linear-gradient(90deg, rgba(224,122,0,0) 0%, var(--orange) 18%, var(--orange) 82%, rgba(224,122,0,0) 100%);
    text-align: center;
    font-family: "Montserrat", Arial, sans-serif;
    font-weight: 800;
    font-size: 34px;
    line-height: 50px;
    color: var(--ink);
  }
  .menu {
    position: absolute;
    left: 60px;
    top: 0;
    margin: 0;
    padding: 0;
  }
  .item-name, .item-price {
    position: absolute;
    left: 0;
    white-space: nowrap;
    margin: 0;
    font-family: "Archivo Black", Arial, sans-serif;
    font-weight: 400;
    line-height: 1;
  }
  .item-name {
    font-size: 46px;
    color: var(--orange);
  }
  .item-price {
    font-size: 33px;
    color: var(--white);
  }
  .special-offer {
    position: absolute;
    left: 626px;
    top: 962px;
    width: 190px;
    height: 190px;
    border-radius: 50%;
    background: var(--orange);
    border: 6px solid var(--ink);
    box-sizing: border-box;
    display: flex;
    align-items: center;
    justify-content: center;
    text-align: center;
    font-family: "Archivo Black", Arial, sans-serif;
    font-size: 32px;
    line-height: 1.2;
    color: var(--ink);
  }
</style>
</head>
<body>
<main class="poster">
  <div class="haunted-house" role="img" aria-label="Dark haunted Victorian house illustration"></div>
  <div class="blood-moon" role="img" aria-label="Red full moon"></div>
  <div class="pumpkins" role="img" aria-label="Glowing carved jack-o'-lanterns on the ground"></div>

  <h1 class="title">
    <svg width="841" height="150" viewBox="0 0 841 150" aria-label="HALLOWEEN">
      <text class="title-text" x="84" y="128" textLength="672" lengthAdjust="spacingAndGlyphs">HALLOWEEN</text>
    </svg>
  </h1>
  <p class="subtitle">EVENT</p>
  <div class="price-band">PRICE LIST</div>

  <div class="menu">
    <p class="item-name" style="top:374px">BRACELETS</p>
    <p class="item-price" style="top:428px">$8 FOR 1, 4 FOR $20</p>
    <p class="item-name" style="top:484px">TOYS</p>
    <p class="item-price" style="top:538px">$15 FOR 1, $20 FOR 2 |</p>
    <p class="item-name" style="top:594px">POPCORN</p>
    <p class="item-price" style="top:652px">$5</p>
    <p class="item-name" style="top:718px">COTTON CANDY</p>
    <p class="item-price" style="top:778px">$5</p>
    <p class="item-name" style="top:834px">CIDER</p>
    <p class="item-price" style="top:892px">$4</p>
  </div>

  <div class="special-offer">SPECIAL<br>OFFER</div>
</main>
</body>
</html>
```